Web site - 5-8 page

We are a small, fresh pasta business called The Noodle Lark located in suburbs of Sacramento, CA. We sell our pasta, ravioli, meatballs and sauce at farmer's markets, events, and soon in our café & marketplace. (Jan 2014) . We also provide catering services. The site needs to communicate FRESH, local, no preservatives, artisan quality pasta. We offer vegetarian, vegan and gluten free products as well.

We would like a web site using our logos and colors to feature what we do, and where people can come buy it. A page to our standard take and make items/menu, our seasonal take and make menu, our catering menu, our new hot food café menu.

We want a page that we can update with "Where can you find The Noodle Lark"
A "specials page" and a page they can order from that they choose the location to pick it up or in the delivery area we deliver to them.
A page with photo's and referrals, testimony, comments, about us, etc. Maybe a page for recipes.
We need to update the events/find us page all the time, weekly, so it needs to be easy for us to go in and do that. We are Window's (not MAC) users if that makes a difference or not, not sure.

Ideally, the same person(s) that make the website would also do a separate project creating our catering and hot food menu brochure/layout and recipe cards

Reason: allow enough time for good quality work

I would like to see the landing page have the pasta shapes/sizes element that is found in the refrigerator wrap, the wrap on the trailer, and the menu - see photo and uploads. It's used as a banner or as a background, bright green.

                                   

 

Would like visitors to be able to "like" me or follow me from my web page. A button or a link?

                                        http://www.brightpantry-example.com/our-food/

Really like the layout of this site. More grocery oriented than café, but we are a take and make marketplace as well as a Panini salads and hot pasta menu for lunch.

Please add Café + Marketplace to headers. Our logo is good but we are now adding a café element and a fresh marketplace, se we need to communicate what we are/what we do. We think adding Café + Marketplace as a descriptor will help. Any ideas, feel free to put your own spin on it. Thank you!!

The designs are good...thanks to everyone!

Reason: To allow for the many updates we have added. Good designs coming in, thank you!

Target Market(s)

#1, busy mom's, busy family's (FAST, Economical meals, no preservatives, local food)
#2 24-34 yr olds that want fresh, vegetarian, vegan or gluten free meal options (no preservatives, local food)
#3 Fresh pasta lovers - any age. The enjoyment of quality fresh pasta and a good meal experience sharing it with friends and family

Industry/Entity Type

Catering

Font styles to use
Other font styles liked:
• EideticNeoRegular, duffy

Colors
9bcb3c
f78f20
eb1f27

Requirements
Must have
• Address, phone, name, logo, colors
Fresh pasta, ravioli, sauce and meatballs in take and make convenient packages. Stress fresh, preservative free, local ingredients, cooks in 45 SECONDS to 3.5 minutes depending on the pasta cut.
FAST meal
Where to find us page - upcoming events
A "specials" page
A page for recipe, how to cook our pasta, how to freeze and store fresh pasta,
How to order online page
Nice to have
• Testimony, links to Facebook, twitter, etc. Place for photo's of product, recent events, customer comments on how they used the product to create their recipe.
Should not have
• No stock photo's of tomato's, no dried pasta images, no Italian flags. No cheesy old world Italian loo or feel. Think fresh, modern, FAST!

```html
<!DOCTYPE html>
<html lang="en">
<head>
<meta charset="utf-8">
<title>The Noodle Lark – Café &amp; Marketplace</title>
<link rel="stylesheet" href="https://fonts.googleapis.com/css2?family=Bungee+Outline&family=Kalam:wght@400&family=Lobster&family=Merriweather:wght@400&family=Questrial&family=Roboto:wght@700&family=Lato:wght@400;700&display=swap">
<style>
  :root {
    --lime: #9bcb3c;
    --band-green: #c0d93a;
    --orange: #f78f20;
    --red: #eb1f27;
    --bright-red: #f21c0c;
    --yellow: #fdb813;
    --cream: #fbf9ec;
    --ink: #3a3a3a;
    --muted: #7a7a6e;
    --dark-green: #2f4a12;
    --white: #ffffff;
  }
  * { box-sizing: border-box; margin: 0; padding: 0; }
  html, body { width: 1073px; height: 1200px; overflow: hidden; }
  body {
    position: relative;
    background: var(--cream);
    font-family: "Lato", sans-serif;
    color: var(--ink);
  }

  .top-band {
    position: absolute; left: 0; top: 0; width: 1073px; height: 160px;
    background: var(--band-green);
  }
  .top-band-edge { position: absolute; left: 0; top: 159px; }

  .utility-links {
    position: absolute; left: 116px; top: 200px;
    display: flex; gap: 22px;
    font-family: "Merriweather", serif; font-size: 14px; color: var(--ink);
  }
  .utility-links span { display: flex; align-items: center; gap: 8px; }

  .phone {
    position: absolute; left: 774px; top: 192px;
    display: flex; align-items: center; gap: 12px;
    font-family: "Merriweather", serif; font-size: 24px; color: var(--ink);
  }

  .brand-name {
    position: absolute; left: 0; width: 1073px; top: 172px;
    text-align: center;
    font-family: "Lobster", cursive; font-size: 50px; color: var(--red);
  }
  .tagline {
    position: absolute; left: 0; width: 1073px; top: 236px;
    text-align: center;
    font-family: "Kalam", cursive; font-size: 32px; color: #222;
  }
  .descriptor {
    position: absolute; left: 0; width: 1073px; top: 304px;
    text-align: center;
    font-family: "Bungee Outline", sans-serif; font-size: 46px; color: var(--red);
    letter-spacing: 1px;
  }

  .main-nav {
    position: absolute; left: 84px; top: 394px; width: 900px; height: 74px;
    display: grid;
    grid-template-columns: 87px 64px 69px 121px 88px 79px 85px 86px 62px 76px 83px;
    background: linear-gradient(#f98a2c, #f0481f 60%, #e9301d);
    border: 1px solid #5a1a0c;
  }
  .main-nav a {
    display: flex; align-items: center; justify-content: center; text-align: center;
    font-family: "Questrial", sans-serif; font-size: 14px; line-height: 16px;
    color: var(--white); text-decoration: none; text-transform: uppercase;
    border-right: 1px solid rgba(255,255,255,.35);
  }
  .main-nav a:last-child { border-right: 0; }

  .hero {
    position: absolute; left: 84px; top: 493px; width: 900px; height: 354px;
    border: 5px solid var(--orange); background: var(--white);
  }
  .hero-photo {
    position: absolute; left: 0; top: 0; width: 567px; height: 344px;
    background: linear-gradient(120deg, #e6d9c5 0%, #f1e3b4 40%, #e8c97a 65%, #9a8b73 100%);
  }
  .hero-figure {
    position: absolute; left: 571px; top: 11px; width: 180px; height: 192px;
    background: linear-gradient(160deg, #f3d6cf, #e9a191);
  }
  .hero-claim {
    position: absolute; left: 545px; top: 210px; width: 290px;
    text-align: center;
    font-family: "Roboto", sans-serif; font-weight: 700; font-size: 26px; line-height: 27px;
    color: var(--red);
  }
  .slider-arrow { position: absolute; top: 129px; }
  .slider-arrow.prev { left: -5px; }
  .slider-arrow.next { right: -5px; }

  .value-strip { position: absolute; left: 84px; top: 868px; }
  .value-strip text {
    font-family: "Questrial", sans-serif; font-size: 24px; fill: var(--white);
  }

  .find-us {
    position: absolute; left: 84px; top: 962px; width: 249px; height: 110px;
    background: var(--bright-red); border: 1px solid #a30d05;
    padding: 8px;
  }
  .find-us-inner {
    height: 100%; border: 1.5px solid rgba(255,255,255,.8);
    display: flex; flex-direction: column; align-items: center; justify-content: center;
    color: var(--white); font-family: "Questrial", sans-serif; text-align: center;
  }
  .find-us-inner .small { font-size: 16px; line-height: 19px; }
  .find-us-inner .big { font-family: "Roboto", sans-serif; font-weight: 700; font-size: 25px; line-height: 30px; }

  .side-menu { position: absolute; left: 84px; top: 1081px; width: 249px; }
  .side-menu h2 {
    height: 47px; background: var(--lime);
    text-align: center; line-height: 47px;
    font-family: "Lato", sans-serif; font-weight: 700; font-size: 26px; color: var(--dark-green);
  }
  .side-menu .category {
    height: 42px; background: linear-gradient(#f1f1ef, #e3e3df);
    border-bottom: 1px solid #cfcfc8;
    display: flex; align-items: center; gap: 10px; padding-left: 18px;
    font-family: "Merriweather", serif; font-size: 17px; color: #333;
  }
  .side-menu .item {
    height: 40px; background: #f4f4f1;
    display: flex; align-items: center; gap: 10px; padding-left: 26px;
    font-family: "Merriweather", serif; font-size: 13px; color: #444;
  }

  .welcome { position: absolute; left: 365px; top: 985px; width: 581px; }
  .welcome h1 {
    text-align: center; font-weight: 400; white-space: nowrap;
    font-family: "Lobster", cursive; font-size: 34px; color: var(--orange);
  }
  .welcome h1 .lead { color: var(--muted); font-size: 27px; }
  .welcome .divider { display: block; margin: 6px 0 8px; }
  .welcome p { font-size: 15px; line-height: 20px; color: #444; }
  .welcome .read-more {
    display: block; text-align: right; margin: 12px 13px 0 0;
    font-size: 13px; color: var(--red); text-decoration: underline;
  }
</style>
</head>
<body>

<div class="top-band" role="img" aria-label="Bright green banner patterned with fresh pasta shapes"></div>
<svg class="top-band-edge" width="1073" height="12" viewBox="0 0 1073 12" aria-hidden="true">
  <defs>
    <pattern id="teeth" width="12" height="12" patternUnits="userSpaceOnUse">
      <polygon points="0,0 12,0 6,11" fill="#c0d93a"/>
    </pattern>
  </defs>
  <rect width="1073" height="12" fill="url(#teeth)"/>
</svg>

<div class="utility-links">
  <span>
    <svg width="24" height="24" viewBox="0 0 24 24" aria-hidden="true"><circle cx="12" cy="8" r="5" fill="#555"/><path d="M3 23c0-6 4-9 9-9s9 3 9 9z" fill="#c33"/></svg>
    My Account
  </span>
  <span>
    <svg width="26" height="24" viewBox="0 0 26 24" aria-hidden="true"><path d="M1 3h4l3 12h13l3-9H7" fill="none" stroke="#d22" stroke-width="2.4"/><circle cx="10" cy="20" r="2.2" fill="#333"/><circle cx="19" cy="20" r="2.2" fill="#333"/></svg>
    My Cart
  </span>
</div>

<div class="phone">
  <svg width="34" height="40" viewBox="0 0 34 40" aria-hidden="true"><path d="M8 3c-4 2-6 6-4 12 3 9 9 17 16 21 4 2 7 1 9-2l-6-7-4 3c-4-3-7-8-8-12l4-3z" fill="#d0211b"/><rect x="4" y="35" width="26" height="3" rx="1.5" fill="#d0211b"/></svg>
  555.014.2298
</div>

<div class="brand-name">The Noodle Lark</div>
<div class="tagline">Freshly Simple</div>
<div class="descriptor">Café &amp; Marketplace</div>

<nav class="main-nav">
  <a href="#">Catering<br>Services</a>
  <a href="#">Cafe<br>Menu</a>
  <a href="#">Fresh<br>Pasta</a>
  <a href="#">Marketplace<br>Menu</a>
  <a href="#">Location<br>Hours</a>
  <a href="#">Recipes<br>History</a>
  <a href="#">Blog<br>Archieve</a>
  <a href="#">Coming<br>Soon</a>
  <a href="#">Pasta<br>Club</a>
  <a href="#">Friends<br>Page</a>
  <a href="#">About<br>Contact</a>
</nav>

<section class="hero">
  <div class="hero-photo" role="img" aria-label="Plate of fresh linguine with peas, pancetta and parsley"></div>
  <div class="hero-figure" role="img" aria-label="Illustrated crowned mascot holding a fork and spoon"></div>
  <p class="hero-claim">FRESH, LOCAL, NO PRESERVATIVES, ARTISAN QUALITY PASTA</p>
  <svg class="slider-arrow prev" width="40" height="90" viewBox="0 0 40 90" aria-label="Previous slide">
    <path d="M0 0a45 45 0 0 1 0 90z" fill="#f78f20"/>
    <path d="M20 37l-8 8 8 8" fill="none" stroke="#fff" stroke-width="3"/>
  </svg>
  <svg class="slider-arrow next" width="40" height="90" viewBox="0 0 40 90" aria-label="Next slide">
    <path d="M40 0a45 45 0 0 0 0 90z" fill="#f78f20"/>
    <path d="M20 37l8 8-8 8" fill="none" stroke="#fff" stroke-width="3"/>
  </svg>
</section>

<svg class="value-strip" width="902" height="88" viewBox="0 0 902 88" aria-label="Fresh Pasta, Local Ingredients, Special Sauce, No Preservatives">
  <defs>
    <linearGradient id="gYellow" x1="0" y1="0" x2="0" y2="1"><stop offset="0" stop-color="#fdc52a"/><stop offset="1" stop-color="#f7a50c"/></linearGradient>
    <linearGradient id="gOrange" x1="0" y1="0" x2="0" y2="1"><stop offset="0" stop-color="#fba94a"/><stop offset="1" stop-color="#f4801a"/></linearGradient>
    <linearGradient id="gGreen" x1="0" y1="0" x2="0" y2="1"><stop offset="0" stop-color="#a6d24a"/><stop offset="1" stop-color="#6fa22a"/></linearGradient>
    <linearGradient id="gRed" x1="0" y1="0" x2="0" y2="1"><stop offset="0" stop-color="#fb3a16"/><stop offset="1" stop-color="#e3160c"/></linearGradient>
  </defs>
  <polygon points="671,0 876,0 900,44 876,88 671,88 695,44" fill="url(#gRed)"/>
  <polygon points="448,0 671,0 695,44 671,88 448,88 472,44" fill="url(#gGreen)"/>
  <polygon points="224,0 448,0 472,44 448,88 224,88 248,44" fill="url(#gOrange)"/>
  <polygon points="0,0 224,0 248,44 224,88 0,88" fill="url(#gYellow)"/>
  <text x="112" y="52" text-anchor="middle">Fresh Pasta</text>
  <text x="340" y="52" text-anchor="middle">Local Ingredients</text>
  <text x="565" y="52" text-anchor="middle">Special Sauce</text>
  <text x="784" y="52" text-anchor="middle">No Preservatives</text>
</svg>

<a class="find-us" href="#">
  <div class="find-us-inner">
    <span class="small">where can you find</span>
    <span class="big">THE NOODLE LARK</span>
    <span class="small">click here</span>
  </div>
</a>

<aside class="side-menu">
  <h2>Our Menu</h2>
  <div class="category">
    <svg width="10" height="10" viewBox="0 0 10 10" aria-hidden="true"><polygon points="5,0 10,3 10,7 5,10 0,7 0,3" fill="#444"/></svg>
    Fresh Pasta
  </div>
  <div class="item">
    <svg width="6" height="6" viewBox="0 0 6 6" aria-hidden="true"><circle cx="3" cy="3" r="3" fill="#666"/></svg>
    Basil
  </div>
</aside>

<section class="welcome">
  <h1><span class="lead">Welcome to</span> The Noodle Lark- Freshly Simple</h1>
  <svg class="divider" width="581" height="14" viewBox="0 0 581 14" aria-hidden="true">
    <line x1="0" y1="7" x2="270" y2="7" stroke="#9bcb3c" stroke-width="1"/>
    <line x1="298" y1="7" x2="569" y2="7" stroke="#9bcb3c" stroke-width="1"/>
    <path d="M284 12l-5-5a3 3 0 0 1 5-3 3 3 0 0 1 5 3z" fill="#9bcb3c"/>
  </svg>
  <p>Beciegast nveriti vitaesaert asety kertya aset aplica boserde nerafae kertyurauestyasnemo faserani iasera ptaiadeser daesraeds. Casrolern atur aut oditaut. onsequuntur magni dolqui ratione voluptatemsequi nesciunt orasario numquam eius modi teincidunt, ut labore et dolore magnam lijaseras. Beciegast nveriti vitaesaert asety kertya aset aplica boserde nerafae kertyurauestyasnemo faserani iasera ptaiadeser daesraeds.</p>
  <a class="read-more" href="#">Read More</a>
</section>

</body>
</html>
```